New Business Card

Would like a shiny card with Metallic logo raised on th front. Address 418 Kestwick Lane, Toronto Ontario M4T2B8, phone 416 555 0382, email kmvc@lorentel.ca and web www.kmvc.ca on the back in right and left lower corners balanced. Top of back should say Personalized Care for Pet's and their People centered. Leaving space on the back to write. Horizontal placement

```html
<!DOCTYPE html>
<html lang="en">
<head>
<meta charset="utf-8">
<title>Kestwick Meadow Veterinary Clinic – Business Card</title>
<link href="https://fonts.googleapis.com/css2?family=Arimo:wght@400;700&display=swap" rel="stylesheet">
<style>
  :root {
    --page-bg: #1d1d1f;
    --card-top: #141414;
    --card-bottom: #050505;
    --ink-white: #ffffff;
    --ink-metal: #8e8e92;
    --ink-soft: #e6e6e6;
    --write-area: #ffffff;
  }
  * { box-sizing: border-box; margin: 0; padding: 0; }
  html, body {
    width: 1200px; height: 1200px; overflow: hidden;
    background: var(--page-bg);
    font-family: "Arimo", Arial, sans-serif;
  }
  .sheet {
    width: 1200px; height: 1200px;
    display: flex; flex-direction: column; align-items: center; justify-content: center;
    gap: 60px;
  }
  .card {
    position: relative;
    width: 840px; height: 480px;
    background: linear-gradient(160deg, var(--card-top), var(--card-bottom));
    box-shadow: 0 18px 40px rgba(0,0,0,.55);
    overflow: hidden;
  }
  /* Front */
  .card--front { display: flex; align-items: center; justify-content: center; }
  .brand { display: flex; align-items: center; gap: 22px; color: var(--ink-metal); }
  .brand__dot { width: 46px; height: 46px; border-radius: 50%; background: var(--ink-metal); }
  .brand__text { text-align: center; font-weight: 400; }
  .brand__name { font-size: 44px; letter-spacing: 3px; line-height: 1; }
  .brand__rule { height: 2px; background: var(--ink-metal); margin: 10px 0 8px; }
  .brand__sub { font-size: 17px; letter-spacing: 4px; }
  /* Back */
  .tagline { position: absolute; top: 34px; left: 0; right: 0; text-align: center; color: var(--ink-white); font-weight: 700; }
  .tagline__lead { font-size: 22px; letter-spacing: 1.5px; }
  .tagline__main { font-size: 40px; letter-spacing: 1px; margin-top: 2px; }
  .write-area {
    position: absolute; left: 56px; right: 56px; top: 140px; height: 226px;
    background: var(--write-area); border-radius: 44px;
  }
  .contact { position: absolute; bottom: 34px; color: var(--ink-soft); font-size: 19px; line-height: 1; }
  .contact--left { left: 56px; }
  .contact--right { right: 56px; text-align: right; }
  .contact__row { display: flex; align-items: center; gap: 10px; margin-top: 12px; }
  .contact--right .contact__row { justify-content: flex-end; }
  .icon { width: 26px; height: 26px; flex: none; }
</style>
</head>
<body>
<main class="sheet">
  <section class="card card--front" aria-label="Card front">
    <div class="brand">
      <span class="brand__dot" aria-hidden="true"></span>
      <div class="brand__text">
        <div class="brand__name">KESTWICK MEADOW</div>
        <div class="brand__rule"></div>
        <div class="brand__sub">VETERINARY CLINIC</div>
      </div>
    </div>
  </section>

  <section class="card card--back" aria-label="Card back">
    <div class="tagline">
      <div class="tagline__lead">PERSONALIZED CARE FOR</div>
      <div class="tagline__main">PET'S AND THEIR PEOPLE</div>
    </div>
    <div class="write-area" aria-label="Space for handwritten notes"></div>

    <div class="contact contact--left">
      <div class="contact__row">
        <svg class="icon" viewBox="0 0 26 26" aria-hidden="true"><circle cx="13" cy="13" r="11.5" fill="none" stroke="#e6e6e6" stroke-width="1.6"/><path d="M9.5 7.5l2 .2 1 3-1.4 1.1a7 7 0 0 0 3.1 3.1l1.1-1.4 3 1 .2 2c-.3.9-1.2 1.5-2.2 1.4-4.4-.6-7.7-3.9-8.3-8.3-.1-1 .5-1.9 1.5-2.1z" fill="#e6e6e6"/></svg>
        <span>416 555 0382</span>
      </div>
      <div class="contact__row">
        <svg class="icon" viewBox="0 0 26 26" aria-hidden="true"><circle cx="13" cy="13" r="11.5" fill="none" stroke="#e6e6e6" stroke-width="1.6"/><path d="M13 6.5a4.5 4.5 0 0 0-4.5 4.5c0 3.4 4.5 8.5 4.5 8.5s4.5-5.1 4.5-8.5A4.5 4.5 0 0 0 13 6.5z" fill="#e6e6e6"/><circle cx="13" cy="11" r="1.7" fill="#0a0a0a"/></svg>
        <span>418 Kestwick Lane, Toronto Ontario M4T2B8</span>
      </div>
    </div>

    <div class="contact contact--right">
      <div class="contact__row">
        <span>kmvc@lorentel.ca</span>
        <svg class="icon" viewBox="0 0 26 26" aria-hidden="true"><circle cx="13" cy="13" r="11.5" fill="none" stroke="#e6e6e6" stroke-width="1.6"/><rect x="7" y="9" width="12" height="8.5" rx="1" fill="#e6e6e6"/><path d="M7.5 9.6l5.5 4.3 5.5-4.3" fill="none" stroke="#0a0a0a" stroke-width="1.2"/></svg>
      </div>
      <div class="contact__row">
        <span>www.kmvc.ca</span>
        <svg class="icon" viewBox="0 0 26 26" aria-hidden="true"><circle cx="13" cy="13" r="11.5" fill="none" stroke="#e6e6e6" stroke-width="1.6"/><g fill="none" stroke="#e6e6e6" stroke-width="1.2"><circle cx="13" cy="13" r="6.5"/><ellipse cx="13" cy="13" rx="2.8" ry="6.5"/><path d="M6.5 13h13M7.5 9.8h11M7.5 16.2h11"/></g></svg>
      </div>
    </div>
  </section>
</main>
</body>
</html>
```